Wine labels Velmora Wine Council - Nueva etiqueta El Consejo Regulador de vinos de Albarrán

Velmora Wines Council, based in southern Spain, are looking to create a new suite of wine labels which retain the elegance of the Sherry Wines industry while reinvigorating their image to the modern era and a new generation of Sherry Wine lovers. These labels will be used across the Velmora Wines Council's range of wines for the promotion of the Sherry Wines industry.

Your design must present at least two styles of Sherry Wines which demonstrate an elegant, modern interpretation and understanding of the unique mood and personality for these wines and the essence of southern Spain.

10 labels will be created based on the winning design, one for each of the unique varieties of Sherry Wines within the collection. This collection comprises of several different wine varieties including: Fino, Manzanilla, Amontillado, Oloroso, Palo Cortado, Medium, Cream, Pale Cream, Pedro Ximenez and Moscatel.

We recommend you visit our website www.velmora-vinos.example/wines as the source to understanding the origins and unique personality of these diverse wines.

El Consejo Regulador de los Vinos de Albarrán y Tordesal quiere renovar las etiquetas de los vinos utilizados para sus actividades de promoción genérica. Esta colección de vinos comprende las tipologías más importantes de la región que incluye: fino, manzanilla, amontillado, oloroso, palo cortado, pale cream, medium, cream, pedro ximénez y moscatel. Por lo tanto se precisan 10 etiquetas, una para cada uno de los vinos mencionados.
Updates

Project Deadline Extended
Reason: Due to some confusion with the deadline we wish to officially extend the deadline to allow designers one last week to submit their entries.

Target Market(s)

Industry, journalists, media, sommeliers, chefs, wine writers

Industry/Entity Type

Council

Requirements
Must have
• Front and Back label plus capsule:
• Front label can have either of the two official logos of the Velmora Wine council titled Vinos de Albarrán Digital or not, this is optional. Must include: Vino selecionado por el Consejo Regulador de la Denominacion de Origen, Name of the variety of wine eg FINO, percentage of alcohol eg 15% and quantity 75 cl.
• The back of the label must include the council logo titled Sellora and 4 additional logos positioned smaller. The Europa logo must appear larger than the 3 other logos. Space for descriptive text about the wine is also required.
• The dimensions of the bottle can be found at this link http://www.vidrialto.example/es/catalogo/vinos-y-espumosos/bordelesas/bd-orla
• Altura:305 mm
• Diámetro base:76,20 mm
• Diámetro hombro:82 mm
• Tipo boca:Cetie
• Peso:750 gr
• Capacidad:75 cl
• Etiqueta delantera y trasera y capsula
• La etiqueta delantera puede incluir el logo oficial del Consejo Regulador o el logo digital, o ninguno, esto es opcional. Debe incluir el siguiete texto: Vino selecionado por el Consejo Regulador de la Denominacion de Origen, el nombre de la variedad del vino, por ejemplo Fino, el porcentaje de alcohol, por ejemplo 15%, y la capacidad 75cl.
• La etiqueta trasera debe incluir el logo oficial Sellora del Consejo, y cuatro logos adicionales con una dimension menor. El Logo de ¨Europa invierte en las zonas rurales¨ debe ser de mayor tamaño que los otros. Se precisa espacio para el texto descriptivo de los vinos.
• Las dimensiones de la botella se puede encontrar en este enlace
• http://www.vidrialto.example/es/catalogo/vinos-y-espumosos/bordelesas/bd-orla
• Altura:305 mm
• Diámetro base:76,20 mm
• Diámetro hombro:82 mm
• Tipo boca:Cetie
• Peso:750 gr
• Capacidad:75 cl
Nice to have
• See our website velmora-vinos.example to understand the origin of the wines. Ver nuestra página web velmora-vinos.example para mejor entender los vinos.
Should not have
• Images of catavinos or stereotypical images from Spain such as flamenco dancers or guitars.

```html
<!DOCTYPE html>
<html lang="es">
<head>
<meta charset="utf-8">
<title>Velmora Wine Council – Etiquetas</title>
<link rel="stylesheet" href="https://fonts.googleapis.com/css2?family=Anton&family=Libre+Caslon+Text:wght@400;700&family=Poppins:wght@700&display=swap">
<style>
  :root{
    --canvas:#f3f0e9;
    --serif:"Libre Caslon Text", Georgia, serif;
    --display:"Anton", Impact, sans-serif;
    --sans:"Poppins", Arial, sans-serif;
  }
  *{box-sizing:border-box;margin:0;padding:0}
  html,body{width:1200px;height:1200px;overflow:hidden;background:var(--canvas)}
  .sheet{position:relative;width:1200px;height:1200px}
  .row{position:absolute;left:60px;width:1080px;display:flex;justify-content:space-between}
  .row--hero{top:40px;height:820px}
  .row--range{top:900px;height:260px}

  .label{position:relative;overflow:hidden;background:var(--band);color:var(--ink);font-size:24px}
  .row--hero .label{width:340px;height:820px}
  .row--range .label{width:99px;height:260px;font-size:7px}

  .label__pattern{position:absolute;left:0;top:0;width:100%;height:58%;
    background:radial-gradient(circle at 30% 40%,var(--pat2) 0%,var(--pat) 70%)}
  .label__head{position:absolute;top:.8em;left:0;width:100%;text-align:center;color:var(--head);font-family:var(--serif)}
  .label__title{font-size:1.05em;letter-spacing:.01em;line-height:1.15;white-space:nowrap}
  .label__sub{font-size:.32em;letter-spacing:.01em;white-space:nowrap}
  .label__mark{position:absolute;top:17%;left:0;width:100%;text-align:center;font-family:var(--display);
    font-size:10.5em;line-height:1;color:var(--band);white-space:nowrap}
  .label__name{position:absolute;top:62.5%;width:100%;text-align:center;font-family:var(--sans);font-size:1.5em;color:var(--ink);white-space:nowrap}
  .label__council{position:absolute;top:75%;width:100%;display:flex;align-items:center;justify-content:center;gap:.35em;
    font-family:var(--serif);font-size:1em;letter-spacing:.3em;color:var(--ink)}
  .label__council i{display:block;width:.6em;height:.6em;background:var(--ink)}
  .label__foot{position:absolute;bottom:3%;left:5%;right:5%;display:flex;justify-content:space-between;align-items:baseline;
    font-family:var(--sans);color:var(--ink)}
  .label__vol{font-size:1.5em}
  .label__abv{font-size:1.1em}

  .fino{--pat:#d6a53a;--pat2:#e4bb55;--band:#2a211b;--ink:#f1d983;--head:#3a2a15}
  .moscatel{--pat:#e4e47a;--pat2:#eeee9a;--band:#838144;--ink:#ecec8c;--head:#6e6c37}
  .palo{--pat:#1f2624;--pat2:#2e3634;--band:#c7ccd3;--ink:#1f2624;--head:#d7dbe0}
  .manzanilla{--pat:#e9e4b4;--pat2:#f3efcc;--band:#2b2a22;--ink:#dcd99c;--head:#4a4830}
  .px{--pat:#9b9b9b;--pat2:#bdbdbd;--band:#1c1c1c;--ink:#f2f2f2;--head:#2a2a2a}
  .medium{--pat:#e3dca0;--pat2:#eee8bd;--band:#f4f0d2;--ink:#4a4530;--head:#6a6240}
  .cream{--pat:#a0976a;--pat2:#b3aa7f;--band:#f1e8c1;--ink:#7a704a;--head:#efe6bf}
  .oloroso{--pat:#8c384c;--pat2:#a04a5e;--band:#f1ece8;--ink:#7a2a3e;--head:#f1dde2}
  .amontillado{--pat:#767676;--pat2:#8d8d8d;--band:#f2f2ef;--ink:#3a3a3a;--head:#eeeeee}
  .pale{--pat:#d6dda5;--pat2:#e3e9bd;--band:#eef0cf;--ink:#8a9a55;--head:#8a9a55}
</style>
</head>
<body>
<main class="sheet">

  <section class="row row--hero">
    <article class="label fino">
      <div class="label__pattern" role="img" aria-label="Damask floral pattern in gold tones"></div>
      <header class="label__head"><p class="label__title">VINO SELECIONADO</p><p class="label__sub">POR EL CONSEJO REGULADOR DE LA DENOMINACIÓN DE ORIGEN</p></header>
      <div class="label__mark">FI</div>
      <h2 class="label__name">Fino</h2>
      <div class="label__council"><i></i>VELMORA</div>
      <footer class="label__foot"><span class="label__vol">75cl</span><span class="label__abv">15%vol</span></footer>
    </article>
    <article class="label moscatel">
      <div class="label__pattern" role="img" aria-label="Damask floral pattern in pale yellow tones"></div>
      <header class="label__head"><p class="label__title">VINO SELECIONADO</p><p class="label__sub">POR EL CONSEJO REGULADOR DE LA DENOMINACIÓN DE ORIGEN</p></header>
      <div class="label__mark">MO</div>
      <h2 class="label__name">Moscatel</h2>
      <div class="label__council"><i></i>VELMORA</div>
      <footer class="label__foot"><span class="label__vol">75cl</span><span class="label__abv">15%vol</span></footer>
    </article>
    <article class="label palo">
      <div class="label__pattern" role="img" aria-label="Damask floral pattern in charcoal tones"></div>
      <header class="label__head"><p class="label__title">VINO SELECIONADO</p><p class="label__sub">POR EL CONSEJO REGULADOR DE LA DENOMINACIÓN DE ORIGEN</p></header>
      <div class="label__mark">PC</div>
      <h2 class="label__name">Palo Cortado</h2>
      <div class="label__council"><i></i>VELMORA</div>
      <footer class="label__foot"><span class="label__vol">75cl</span><span class="label__abv">15%vol</span></footer>
    </article>
  </section>

  <section class="row row--range">
    <article class="label fino">
      <div class="label__pattern" role="img" aria-label="Damask floral pattern in gold tones"></div>
      <header class="label__head"><p class="label__title">VINO SELECIONADO</p><p class="label__sub">POR EL CONSEJO REGULADOR DE LA DENOMINACIÓN DE ORIGEN</p></header>
      <div class="label__mark">FI</div><h2 class="label__name">Fino</h2>
      <div class="label__council"><i></i>VELMORA</div>
      <footer class="label__foot"><span class="label__vol">75cl</span><span class="label__abv">15%vol</span></footer>
    </article>
    <article class="label manzanilla">
      <div class="label__pattern" role="img" aria-label="Damask floral pattern in pale cream tones"></div>
      <header class="label__head"><p class="label__title">VINO SELECIONADO</p><p class="label__sub">POR EL CONSEJO REGULADOR DE LA DENOMINACIÓN DE ORIGEN</p></header>
      <div class="label__mark">MA</div><h2 class="label__name">Manzanilla</h2>
      <div class="label__council"><i></i>VELMORA</div>
      <footer class="label__foot"><span class="label__vol">75cl</span><span class="label__abv">15%vol</span></footer>
    </article>
    <article class="label palo">
      <div class="label__pattern" role="img" aria-label="Damask floral pattern in charcoal tones"></div>
      <header class="label__head"><p class="label__title">VINO SELECIONADO</p><p class="label__sub">POR EL CONSEJO REGULADOR DE LA DENOMINACIÓN DE ORIGEN</p></header>
      <div class="label__mark">PC</div><h2 class="label__name">Palo Cortado</h2>
      <div class="label__council"><i></i>VELMORA</div>
      <footer class="label__foot"><span class="label__vol">75cl</span><span class="label__abv">15%vol</span></footer>
    </article>
    <article class="label px">
      <div class="label__pattern" role="img" aria-label="Damask floral pattern in grey tones"></div>
      <header class="label__head"><p class="label__title">VINO SELECIONADO</p><p class="label__sub">POR EL CONSEJO REGULADOR DE LA DENOMINACIÓN DE ORIGEN</p></header>
      <div class="label__mark">PX</div><h2 class="label__name">Pedro Ximenez</h2>
      <div class="label__council"><i></i>VELMORA</div>
      <footer class="label__foot"><span class="label__vol">75cl</span><span class="label__abv">15%vol</span></footer>
    </article>
    <article class="label medium">
      <div class="label__pattern" role="img" aria-label="Damask floral pattern in straw tones"></div>
      <header class="label__head"><p class="label__title">VINO SELECIONADO</p><p class="label__sub">POR EL CONSEJO REGULADOR DE LA DENOMINACIÓN DE ORIGEN</p></header>
      <div class="label__mark">ME</div><h2 class="label__name">Medium</h2>
      <div class="label__council"><i></i>VELMORA</div>
      <footer class="label__foot"><span class="label__vol">75cl</span><span class="label__abv">15%vol</span></footer>
    </article>
    <article class="label cream">
      <div class="label__pattern" role="img" aria-label="Damask floral pattern in tan tones"></div>
      <header class="label__head"><p class="label__title">VINO SELECIONADO</p><p class="label__sub">POR EL CONSEJO REGULADOR DE LA DENOMINACIÓN DE ORIGEN</p></header>
      <div class="label__mark">CR</div><h2 class="label__name">Cream</h2>
      <div class="label__council"><i></i>VELMORA</div>
      <footer class="label__foot"><span class="label__vol">75cl</span><span class="label__abv">15%vol</span></footer>
    </article>
    <article class="label oloroso">
      <div class="label__pattern" role="img" aria-label="Damask floral pattern in burgundy tones"></div>
      <header class="label__head"><p class="label__title">VINO SELECIONADO</p><p class="label__sub">POR EL CONSEJO REGULADOR DE LA DENOMINACIÓN DE ORIGEN</p></header>
      <div class="label__mark">OL</div><h2 class="label__name">Oloroso</h2>
      <div class="label__council"><i></i>VELMORA</div>
      <footer class="label__foot"><span class="label__vol">75cl</span><span class="label__abv">15%vol</span></footer>
    </article>
    <article class="label amontillado">
      <div class="label__pattern" role="img" aria-label="Damask floral pattern in mid grey tones"></div>
      <header class="label__head"><p class="label__title">VINO SELECIONADO</p><p class="label__sub">POR EL CONSEJO REGULADOR DE LA DENOMINACIÓN DE ORIGEN</p></header>
      <div class="label__mark">AM</div><h2 class="label__name">Amontillado</h2>
      <div class="label__council"><i></i>VELMORA</div>
      <footer class="label__foot"><span class="label__vol">75cl</span><span class="label__abv">15%vol</span></footer>
    </article>
    <article class="label pale">
      <div class="label__pattern" role="img" aria-label="Damask floral pattern in pale green tones"></div>
      <header class="label__head"><p class="label__title">VINO SELECIONADO</p><p class="label__sub">POR EL CONSEJO REGULADOR DE LA DENOMINACIÓN DE ORIGEN</p></header>
      <div class="label__mark">PL</div><h2 class="label__name">Pale Cream</h2>
      <div class="label__council"><i></i>VELMORA</div>
      <footer class="label__foot"><span class="label__vol">75cl</span><span class="label__abv">15%vol</span></footer>
    </article>
    <article class="label moscatel">
      <div class="label__pattern" role="img" aria-label="Damask floral pattern in pale yellow tones"></div>
      <header class="label__head"><p class="label__title">VINO SELECIONADO</p><p class="label__sub">POR EL CONSEJO REGULADOR DE LA DENOMINACIÓN DE ORIGEN</p></header>
      <div class="label__mark">MO</div><h2 class="label__name">Moscatel</h2>
      <div class="label__council"><i></i>VELMORA</div>
      <footer class="label__foot"><span class="label__vol">75cl</span><span class="label__abv">15%vol</span></footer>
    </article>
  </section>

</main>
</body>
</html>
```